Real Estate Search Site Re-Design of 2 Pages

Looking for designs to optimize 2 pages of our current site design. Our site allows users to find properties to purchase or rent.

Basically there are 4 panes
1. The top red one where you actually type in what you''re looking for.
2. The map pane that shows the properties
3. The scrollable results pane.
4. Property details pane.

A typical search would go like this:
1. User fills in their search criteria in the top pane in red. Clicks Find Homes
2. Site updates the map with properties plotted that fit the criteria. Site also populates the results pane at the bottom. Site shows the most newest property that fits the search criteria on the right.
3. User will scroll through the results pane or the map and click a property.
4. Site will update the property details pane with information on the selected property.

Search/Results Page
This main page needs a search form area, a results area, an area to display details of a property selected, a map to show results, and an area to display a real estate agent's information. The design must be full-screen to use all the space on the screen. All information should fit on a 1366x768 screen size. Please see sample screen shot.

Property Details Page
This one can be fixed width of 978px. This page needs all the elements that are displayed in the sample PNG file. Ideally, we want to be able to see all important information without scrolling on a 1366x768 screen. The important information in this size are Pictures with controls, address, bedrooms, bathrooms, square feet, square feet of the lot, days on market, agent information, and buttons to request a showing or get more information.

Our Goal:
Our goal is to get create a different way to display the data in an effective way. We want different ways to show the search results, maybe a vertical, scrolling list of property information with pictures. Or even a horizontal scrolling results pane. It must contain:

1. A map of the results
2. A way to scroll through the search results (like we have currently in case someone wants to search/sort bedrooms or square footage)
3. A way to view details of the property
4. A way to display agent information/picture
Updates

There's a lot of good design work coming through. Thank you.

Perhaps review some other real estate sales sites for ideas on pane configuration. Example site links:
http://www.brovat.example/homes/for_sale/?gclid=QXmP7k2-tb9DHR4W1KzeqN5BCE (brovat.example)
http://www.pemnox.example/?sem=3.4.2.6.8.2.1.15&gclid=RJwz82m-tb9DHWcn4KzeuTpBHS (Pemnox.example)
http://www.quindert.example/map_search/results/i/ (quindert.example)

Our goal for the redesign is to display the data in a more effective way. Either with a better flow, more pictures, more information, smoother search process. Please see the updated brief for details. The main idea is to show the data in the most effective way possible.

Project Deadline Extended
Reason: Still looking at different ideas for the search results. We are still open for fresh ideas.

Industry/Entity Type

Real Estate

Font styles to use
Sans Serif

Colors
eb1f27

```html
<!DOCTYPE html>
<html lang="en">
<head>
<meta charset="utf-8">
<title>Property Details – 1727 Tessaro Avenue</title>
<link rel="stylesheet" href="https://fonts.googleapis.com/css2?family=Open+Sans:wght@400;600&family=Roboto:wght@400&display=swap">
<style>
:root{
  --brand-red:#eb1f27;
  --red-top:#ee4146;
  --red-bottom:#c81d22;
  --deep-red:#b30006;
  --dark:#333333;
  --panel:#ececec;
  --text:#222222;
  --muted:#555555;
  --logo:#f7c27c;
  --white:#ffffff;
  --card-border:#a9a9a9;
}
*{box-sizing:border-box;margin:0;padding:0}
html,body{width:1200px;height:675px;overflow:hidden;background:var(--white)}
body{font-family:"Open Sans",Arial,sans-serif;color:var(--text)}
.stage{position:relative;width:1366px;height:768px;transform:scale(.8785);transform-origin:0 0}
.abs{position:absolute}
.site-header{left:194px;top:1px;width:978px;height:61px;background:linear-gradient(var(--red-top),var(--red-bottom))}
.brand{left:7px;top:8px;font-size:31px;color:var(--logo);font-weight:400}
.lang{top:7px;width:18px;height:14px;border:1px solid var(--white)}
.lang-en{left:925px;background:#2c3f8f}
.lang-es{left:946px;background:linear-gradient(#c60b1e 25%,#ffc400 25% 75%,#c60b1e 75%)}
.main-nav{right:14px;top:36px;display:flex;gap:22px;font-size:15px;color:var(--white)}
.search-bar{left:194px;top:63px;width:978px;height:62px;background:var(--dark);color:var(--white)}
.field-label{top:19px;font-size:18px}
.field{top:18px;height:24px;background:var(--white);color:#8a8a8a;font-size:15px;padding:1px 6px;line-height:22px}
.field.select{background:#f4f4f4}
.field.select::after{content:"";position:absolute;right:6px;top:8px;border:6px solid transparent;border-top:9px solid #222;border-bottom:0}
.btn{background:linear-gradient(#ef3a3f,#c81d22);color:var(--white);font-size:14px;text-align:center;border:1px solid #8d1014;border-radius:2px;text-transform:uppercase}
.find-btn{left:875px;top:18px;width:92px;height:25px;line-height:23px}
.hero-photo{left:194px;top:133px;width:618px;height:411px;background:linear-gradient(#5c96d8 0%,#9cc3e8 30%,#9b8f7d 55%,#4f8a2c 78%,#3f6f1f 100%)}
.slide-arrow{top:187px;width:38px;height:38px;border-radius:50%;background:rgba(255,255,255,.8)}
.thumbs{left:195px;top:549px}
.thumb{position:absolute;top:0;width:83px;height:54px;background:linear-gradient(#d6d0c4,#8b7a66)}
.agent-panel{left:820px;top:135px;width:352px;height:164px;background:var(--panel)}
.agent-role{left:15px;top:7px;font-size:15px}
.agent-license{left:241px;top:5px;font-size:13px}
.agent-photo{left:12px;top:41px;width:85px;height:111px;background:linear-gradient(#e6e9ec,#8aa3b6)}
.agent-info{left:121px;top:38px;font-size:13.5px;line-height:24px}
.agent-btn{top:116px;width:105px;height:28px;line-height:26px}
.similar-bar{left:820px;top:306px;width:352px;height:36px;background:var(--dark);color:var(--white);font-size:17px;padding:5px 10px}
.home-card{top:354px;width:170px;height:251px;border:1px solid var(--card-border);background:var(--white)}
.card-address{left:6px;top:6px;font-size:13.5px;line-height:24px}
.card-photo{left:7px;top:69px;width:154px;height:104px;background:linear-gradient(#6e9fd3,#b9b19c 55%,#4d7b35)}
.card-price{left:7px;top:176px;width:154px;height:20px;background:var(--deep-red);color:var(--white);font-family:Roboto,Arial,sans-serif;font-size:13px;display:flex;justify-content:space-between;padding:1px 4px}
.card-stats{left:7px;top:198px;width:154px;display:flex;font-family:Roboto,Arial,sans-serif;text-align:center}
.stat{flex:1;border-left:1px solid #999}
.stat:first-child{border-left:0;flex:.8}
.stat:nth-child(2){flex:.8}
.stat:last-child{flex:1.4}
.stat b{display:block;font-weight:400;font-size:21px;line-height:24px}
.stat span{display:block;font-size:10px;color:var(--muted)}
.summary{left:194px;top:629px;width:977px;height:102px;background:var(--panel)}
.summary-address{left:18px;top:11px;font-size:23px;color:var(--brand-red)}
.summary-facts{left:17px;top:56px;font-size:19.5px;display:flex;gap:19px}
.info-btn{left:763px;top:53px;width:203px;height:29px;line-height:27px}
</style>
</head>
<body>
<div class="stage">
  <header class="site-header abs">
    <div class="brand abs">Logo Here</div>
    <span class="lang lang-en abs" aria-label="English"></span>
    <span class="lang lang-es abs" aria-label="Español"></span>
    <nav class="main-nav abs"><span>Communities</span><span>Locations</span><span>Contact</span></nav>
  </header>

  <form class="search-bar abs">
    <span class="field-label abs" style="left:9px">Location</span>
    <span class="field abs" style="left:82px;width:112px">Alhambra</span>
    <span class="field-label abs" style="left:204px">Type</span>
    <span class="field select abs" style="left:251px;width:116px">Townhouse</span>
    <span class="field-label abs" style="left:377px">Price</span>
    <span class="field select abs" style="left:421px;width:89px">$500 K</span>
    <span class="field-label abs" style="left:519px">to</span>
    <span class="field select abs" style="left:542px;width:89px">$1 M</span>
    <span class="field-label abs" style="left:643px">Beds</span>
    <span class="field select abs" style="left:690px;width:50px">3+</span>
    <span class="field-label abs" style="left:751px">Baths</span>
    <span class="field select abs" style="left:802px;width:50px">3+</span>
    <span class="btn find-btn abs">Find Home</span>
  </form>

  <section class="hero-photo abs" role="img" aria-label="Front view of a two-storey brick house with lawn and large tree">
    <span class="slide-arrow abs" style="left:5px"><svg width="38" height="38"><path d="M22 11 L14 19 L22 27" stroke="#666" stroke-width="3" fill="none"/></svg></span>
    <span class="slide-arrow abs" style="left:574px"><svg width="38" height="38"><path d="M16 11 L24 19 L16 27" stroke="#666" stroke-width="3" fill="none"/></svg></span>
  </section>
  <div class="thumbs abs">
    <span class="thumb" style="left:0" role="img" aria-label="Living room"></span>
    <span class="thumb" style="left:88px" role="img" aria-label="Dining room"></span>
    <span class="thumb" style="left:176px" role="img" aria-label="Family room"></span>
    <span class="thumb" style="left:266px" role="img" aria-label="Kitchen"></span>
    <span class="thumb" style="left:356px" role="img" aria-label="Kitchen detail"></span>
    <span class="thumb" style="left:446px" role="img" aria-label="Living room"></span>
    <span class="thumb" style="left:534px" role="img" aria-label="Dining room"></span>
  </div>

  <aside class="agent-panel abs">
    <div class="agent-role abs">Buyer's Agent</div>
    <div class="agent-license abs">BRF#04829153</div>
    <div class="agent-photo abs" role="img" aria-label="Agent portrait"></div>
    <div class="agent-info abs">Mara Quell<br>(626) 555-0184<br>Mara@brovelin.example</div>
    <span class="btn agent-btn abs" style="left:121px">Visit Home</span>
    <span class="btn agent-btn abs" style="left:239px">Start Offers</span>
  </aside>

  <div class="similar-bar abs">Similar Homes Nearby
    <svg class="abs" style="right:10px;top:13px" width="14" height="10"><path d="M1 2 L7 8 L13 2" stroke="#fff" stroke-width="2" fill="none"/></svg>
  </div>

  <article class="home-card abs" style="left:819px">
    <div class="card-address abs">1425 Via Corlena Drive<br>Rowland Heig......(91007)</div>
    <div class="card-photo abs" role="img" aria-label="Single-storey home with palms"></div>
    <div class="card-price abs"><span>$2,795,000</span><span>.55 mi</span></div>
    <div class="card-stats abs"><div class="stat"><b>5</b><span>Beds</span></div><div class="stat"><b>3</b><span>Baths</span></div><div class="stat"><b>3,306</b><span>Sq. Ft.</span></div></div>
  </article>
  <article class="home-card abs" style="left:1003px">
    <div class="card-address abs">1425 Via Corlena Drive<br>Rowland Heig......(91007)</div>
    <div class="card-photo abs" role="img" aria-label="Single-storey home with palms"></div>
    <div class="card-price abs"><span>$2,795,000</span><span>.55 mi</span></div>
    <div class="card-stats abs"><div class="stat"><b>5</b><span>Beds</span></div><div class="stat"><b>3</b><span>Baths</span></div><div class="stat"><b>3,306</b><span>Sq. Ft.</span></div></div>
  </article>

  <section class="summary abs">
    <h1 class="summary-address abs" style="font-weight:400">1727 Tessaro Avenue, Rowland Heights CA</h1>
    <div class="summary-facts abs"><span>Price: $2,388,000</span><span>Beds: 3</span><span>Baths: 2.5</span><span>Sq.Ft.: 3,306</span><span>Sq.Ft. Lot: 12,503</span><span>Days: 14</span></div>
    <span class="btn info-btn abs">Get More Information</span>
  </section>
</div>
</body>
</html>
```